Jewelry Back Card Graphic Design

I am looking for a graphic design to print out and put in the back of the jewelry box for my long-distance jewelry. I attached an example that I am now using for the "still harbor jewelry" so you can see what it's used for.

But this card needs to relate to people who are in a long-distance relationship or friendship, so it needs to resonate with them when they see it on the website and open the box if they receive the jewelry as a gift.

I attached a rough idea that I sketched myself, but you can be creative and create anything else if you have a better idea.

It needs to be square.

Looking forward to the results!

```html
<!DOCTYPE html>
<html lang="en">
<head>
<meta charset="UTF-8">
<title>A True Connection Goes Beyond Horizon – Card</title>
<link href="https://fonts.googleapis.com/css2?family=Fascinate+Inline&display=swap" rel="stylesheet">
<style>
  :root {
    --sky-night: #1f2f63;
    --sky-blue: #3a4f86;
    --sky-haze: #7c7f8f;
    --sun-gold: #f2d35a;
    --sun-amber: #f6a43c;
    --sun-coral: #f26b4a;
    --sun-red: #e4472f;
    --sea-rust: #a83a1c;
    --sea-deep: #4a1a10;
    --type-white: #ffffff;
    --type-shadow: rgba(70, 35, 30, 0.6);
  }
  html, body {
    margin: 0;
    padding: 0;
    width: 1200px;
    height: 1200px;
    overflow: hidden;
    background: #ffffff;
  }
  .card {
    position: relative;
    width: 1200px;
    height: 1200px;
    overflow: hidden;
  }
  .sunset-scene {
    position: absolute;
    inset: 0;
    background:
      radial-gradient(ellipse 70% 45% at 50% 92%, rgba(255, 150, 110, 0.75) 0%, rgba(255, 120, 80, 0) 70%),
      linear-gradient(180deg,
        var(--sky-night) 0%,
        var(--sky-blue) 18%,
        var(--sky-haze) 28%,
        var(--sun-gold) 40%,
        var(--sun-amber) 55%,
        var(--sun-coral) 70%,
        var(--sun-red) 86%,
        var(--sea-rust) 87.5%,
        var(--sea-deep) 100%);
  }
  .headline {
    position: absolute;
    left: 0;
    right: 0;
    top: 330px;
    margin: 0;
    text-align: center;
    font-family: "Fascinate Inline", serif;
    font-weight: 400;
    font-size: 100px;
    line-height: 141px;
    color: var(--type-white);
    text-transform: uppercase;
    text-shadow: 0 52px 7px var(--type-shadow);
  }
  .headline-line {
    display: block;
    white-space: nowrap;
  }
</style>
</head>
<body>
  <main class="card">
    <div class="sunset-scene" role="img" aria-label="Painted sunset over the sea: starry night-blue sky fading through golden clouds and sun rays into a glowing orange-red horizon above dark water"></div>
    <h1 class="headline">
      <span class="headline-line">A True</span>
      <span class="headline-line">Connection</span>
      <span class="headline-line">Goes Beyond</span>
      <span class="headline-line">Horizon</span>
    </h1>
  </main>
</body>
</html>
```